Business Card for my New Brokerage

Looking to get a business card design for my new Real Estate Brokerage.
I want it with Picture, Phone Number, Email, Website, Office Address
Name and Designation. Please add logo too.

Target Market(s)

Real Estate Investors or Home Buyers

Industry/Entity Type

Real Estate

Contact Information for Business Card

Name, Email, Phone Number, website, email, office address

Colors
EB3D1F
EC4F4E
F09395
F8D3D4
FCEDEE

Requirements
Must have
• Minimalistic, Clean, Modern, Photo
Nice to have
• White and Red Colors

```html
<!DOCTYPE html>
<html lang="en">
<head>
<meta charset="UTF-8">
<title>Ember Realty Inc – Business Card</title>
<link rel="stylesheet" href="https://fonts.googleapis.com/css2?family=Montserrat:wght@400;500;700;800&display=swap">
<style>
  :root {
    --brand-red: #cc1c23;
    --gold: #b8862b;
    --card-white: #f1f1f2;
    --stage: #e8e9eb;
    --text-grey: #6f6f72;
    --suit-navy: #1f2a44;
  }
  * { margin: 0; padding: 0; box-sizing: border-box; }
  html, body { width: 1200px; height: 1200px; overflow: hidden; }
  body {
    background: var(--stage);
    font-family: "Montserrat", sans-serif;
    position: relative;
  }
  .card {
    position: absolute;
    left: 227px;
    width: 746px;
    height: 425px;
    overflow: hidden;
  }
  .card-front { top: 135px; background: var(--card-white); }
  .card-back { top: 639px; background: var(--brand-red); }

  /* front */
  .side-stripe {
    position: absolute; left: 37px; top: 0; width: 44px; height: 100%;
    background: var(--brand-red);
  }
  .stripe-gap {
    position: absolute; left: 37px; top: 60px; width: 44px; height: 56px;
    background: var(--card-white);
  }
  .stripe-square {
    position: absolute; left: 37px; top: 64px; width: 44px; height: 46px;
    background: var(--gold);
  }
  .brand-front {
    position: absolute; left: 110px; top: 46px;
    color: var(--brand-red); text-align: center; width: 300px;
  }
  .brand-name {
    font-weight: 800; font-size: 72px; line-height: 1; letter-spacing: 1px;
  }
  .brand-sub {
    font-weight: 500; font-size: 21px; letter-spacing: 5px; margin-top: 10px;
  }
  .agent-name {
    position: absolute; left: 112px; top: 183px;
    color: var(--brand-red); font-weight: 700; font-size: 24px;
  }
  .agent-title {
    position: absolute; left: 112px; top: 213px;
    color: var(--text-grey); font-weight: 500; font-size: 18px;
  }
  .office-address {
    position: absolute; left: 112px; top: 263px;
    color: var(--text-grey); font-weight: 500; font-size: 18px; line-height: 27px;
  }
  .contact-list {
    position: absolute; left: 112px; top: 323px; list-style: none;
    color: var(--text-grey); font-weight: 500; font-size: 18px;
  }
  .contact-list li {
    display: flex; align-items: center; gap: 6px; height: 27px;
  }
  .contact-icon { width: 19px; height: 19px; flex: none; }
  .agent-photo {
    position: absolute; left: 461px; top: 22px; width: 285px; height: 403px;
    background: linear-gradient(180deg, var(--card-white) 0%, #c9c2bd 30%, #3a4560 60%, var(--suit-navy) 100%);
  }

  /* back */
  .brand-back {
    position: absolute; left: 0; top: 164px; width: 100%;
    color: var(--card-white); text-align: center;
  }
  .brand-back .brand-name { font-size: 124px; letter-spacing: 2px; }
  .brand-back .brand-sub { font-size: 36px; letter-spacing: 8px; margin-top: 14px; }
</style>
</head>
<body>
  <section class="card card-front">
    <div class="side-stripe"></div>
    <div class="stripe-gap"></div>
    <div class="stripe-square"></div>

    <div class="brand-front">
      <div class="brand-name">EMBER</div>
      <div class="brand-sub">REALTY INC</div>
    </div>

    <div class="agent-name">DANIEL HARTWELL</div>
    <div class="agent-title">Managing Director</div>

    <div class="office-address">145 Maple Avenue,<br>Ste 2, Lakeview, NH 0352</div>

    <ul class="contact-list">
      <li>
        <svg class="contact-icon" viewBox="0 0 20 20" aria-hidden="true">
          <circle cx="10" cy="10" r="10" fill="var(--brand-red)"/>
          <path d="M6.5 5.5l2 .3.6 2.2-1.2.9a7 7 0 0 0 3.2 3.2l.9-1.2 2.2.6.3 2-1.4 1.1C9.6 14.4 5.6 10.4 5.4 6.9z" fill="#fff"/>
        </svg>
        555 0142 873
      </li>
      <li>
        <svg class="contact-icon" viewBox="0 0 20 20" aria-hidden="true">
          <circle cx="10" cy="10" r="10" fill="var(--brand-red)"/>
          <rect x="5" y="6.5" width="10" height="7" fill="none" stroke="#fff" stroke-width="1.3"/>
          <path d="M5 6.5l5 4 5-4" fill="none" stroke="#fff" stroke-width="1.3"/>
        </svg>
        hello@emberrealty.com
      </li>
      <li>
        <svg class="contact-icon" viewBox="0 0 20 20" aria-hidden="true">
          <circle cx="10" cy="10" r="10" fill="var(--brand-red)"/>
          <circle cx="10" cy="10" r="5" fill="none" stroke="#fff" stroke-width="1.3"/>
          <path d="M5 10h10M10 5c-2.5 3-2.5 7 0 10M10 5c2.5 3 2.5 7 0 10" fill="none" stroke="#fff" stroke-width="1"/>
        </svg>
        www.emberrealty.com
      </li>
    </ul>

    <div class="agent-photo" role="img" aria-label="Portrait photo of the managing director in a navy suit and red tie, arms crossed"></div>
  </section>

  <section class="card card-back">
    <div class="brand-back">
      <div class="brand-name">EMBER</div>
      <div class="brand-sub">REALTY INC</div>
    </div>
  </section>
</body>
</html>
```